Shipping cards

Expedited delivery of various business related products , packages ,parcels etc. Intrastate or Interstate.

Target Market(s)

business and or private customer base.with expedited needs and short term or long term needs.

Industry/Entity Type

Business

Contact Information for Business Card

would like the silhouette of my dog between the business name Amber{ } Fox . Amber Fox Freight ,Expedited Delivery, tel330-958-3637 fax TBD , dispatch@quillmail.test, Dennis J. Holt- Owner

Font styles to use
Serif

Requirements
Must have
• dog silhouette between Amber Fox or before and after name of company.
Should not have
• remove oval from silhouette around dog

```html
<!DOCTYPE html>
<html lang="en">
<head>
<meta charset="utf-8">
<title>Amber Fox Freight — Business Cards</title>
<link rel="stylesheet" href="https://fonts.googleapis.com/css2?family=Crimson+Text:wght@400;700&family=Lato:wght@400&family=Oranienbaum&display=swap">
<style>
  :root {
    --backdrop: #ece5da;
    --card-ink: #231f20;
    --card-paper: #ffffff;
    --text-light: #ffffff;
    --text-dark: #111111;
  }
  * { margin: 0; padding: 0; box-sizing: border-box; }
  html, body { width: 1200px; height: 908px; overflow: hidden; }
  body {
    position: relative;
    background: var(--backdrop);
    font-family: "Crimson Text", Georgia, serif;
  }

  .card {
    position: absolute;
    width: 608px;
    height: 356px;
    background: var(--card-ink);
    overflow: hidden;
  }

  /* Front */
  .card--front { left: 192px; top: 52px; }
  .front-mark {
    position: absolute;
    left: 0; right: 0; top: 118px;
    height: 100px;
    display: flex;
    align-items: center;
    justify-content: center;
    gap: 20px;
  }
  .front-mark__dot {
    width: 24px; height: 24px;
    border-radius: 50%;
    background: var(--text-light);
    flex: none;
  }
  .front-mark__name {
    font-family: "Oranienbaum", "Crimson Text", Georgia, serif;
    font-weight: 400;
    font-size: 104px;
    line-height: 1;
    letter-spacing: 0;
    color: var(--text-light);
    text-transform: uppercase;
    white-space: nowrap;
  }
  .front-band {
    position: absolute;
    left: 0; right: 0; bottom: 0;
    height: 42px;
    background: var(--card-paper);
    display: flex;
    align-items: center;
    justify-content: center;
    font-family: "Lato", Arial, sans-serif;
    font-size: 24px;
    letter-spacing: 1px;
    color: var(--text-dark);
    text-transform: uppercase;
  }

  /* Back */
  .card--back { left: 394px; top: 489px; }
  .back-strip {
    position: absolute;
    right: 0; top: 0;
    width: 121px; height: 100%;
    background: var(--card-paper);
    overflow: hidden;
  }
  .back-strip__name {
    position: absolute;
    left: 50%; top: 50%;
    transform: translate(-50%, -50%) rotate(-90deg);
    white-space: nowrap;
    font-family: "Oranienbaum", "Crimson Text", Georgia, serif;
    font-weight: 400;
    font-size: 74px;
    line-height: 1;
    letter-spacing: 0;
    color: var(--text-dark);
    text-transform: uppercase;
  }
  .contact {
    position: absolute;
    left: 27px; top: 110px;
    color: var(--text-light);
  }
  .contact__name { font-weight: 700; font-size: 23px; line-height: 28px; }
  .contact__role { font-size: 21px; line-height: 26px; }
  .contact__company {
    margin-top: 22px;
    font-size: 18px;
    line-height: 22px;
    text-transform: uppercase;
  }
  .contact__lines { margin-top: 10px; list-style: none; }
  .contact__lines li {
    display: flex;
    align-items: center;
    gap: 6px;
    font-size: 17px;
    line-height: 22px;
  }
  .contact__icon { width: 16px; height: 16px; fill: var(--text-light); flex: none; }
</style>
</head>
<body>

  <section class="card card--front" aria-label="Card front">
    <div class="front-mark">
      <span class="front-mark__dot" aria-hidden="true"></span>
      <span class="front-mark__name">Amber Fox</span>
    </div>
    <div class="front-band">Amber Fox Freight</div>
  </section>

  <section class="card card--back" aria-label="Card back">
    <div class="contact">
      <p class="contact__name">Dennis J. Holt</p>
      <p class="contact__role">Owner</p>
      <p class="contact__company">Amber Fox Freight<br>Expedited Delivery</p>
      <ul class="contact__lines">
        <li>
          <svg class="contact__icon" viewBox="0 0 24 24" aria-hidden="true"><path d="M6.6 10.8a15.2 15.2 0 0 0 6.6 6.6l2.2-2.2a1 1 0 0 1 1-.25 11.4 11.4 0 0 0 3.6.57 1 1 0 0 1 1 1V20a1 1 0 0 1-1 1A17 17 0 0 1 3 4a1 1 0 0 1 1-1h3.5a1 1 0 0 1 1 1c0 1.25.2 2.46.57 3.6a1 1 0 0 1-.25 1z"/></svg>
          412-573-2916
        </li>
        <li>
          <svg class="contact__icon" viewBox="0 0 24 24" aria-hidden="true"><path d="M6 2h12v5H6zM3 8h18a1 1 0 0 1 1 1v8h-4v5H6v-5H2V9a1 1 0 0 1 1-1zm5 7v5h8v-5z"/></svg>
          TBD
        </li>
        <li>
          <svg class="contact__icon" viewBox="0 0 24 24" aria-hidden="true"><path d="M2 5h20v14H2zm2 2v.4l8 5.2 8-5.2V7zm0 2.8V17h16V9.8l-8 5.2z"/></svg>
          dispatch@quillmail.test
        </li>
      </ul>
    </div>
    <div class="back-strip">
      <span class="back-strip__name">Amber Fox</span>
    </div>
  </section>

</body>
</html>
```